Established food business needs a new name card design

Refer to attached current name card. Would like a new professional look design with only the company name and logo without any pictures. Would like green and yellow to be included.
To include:
My name "IBRAHIM SUKRI" and hand phone number "87260413".
To delete "
"Along Brackendale Ave 8" and
"www.nur-tiwas.com.sg"
To change email to:
"tkr27@velmorix.com.sg"

```html
<!DOCTYPE html>
<html lang="en">
<head>
<meta charset="utf-8">
<title>Nur-Tiwas Name Card</title>
<link href="https://fonts.googleapis.com/css2?family=Montserrat:wght@500;600;700&display=swap" rel="stylesheet">
<style>
  :root {
    --backdrop: #1f1f1f;
    --card-green: #0f4d36;
    --card-green-light: #1b5c43;
    --accent-yellow: #f7d417;
    --text-white: #ffffff;
  }
  * { box-sizing: border-box; margin: 0; padding: 0; }
  html, body {
    width: 1200px;
    height: 900px;
    overflow: hidden;
    background: var(--backdrop);
    font-family: "Montserrat", sans-serif;
  }
  .stage {
    width: 1200px;
    height: 900px;
    display: flex;
    flex-direction: column;
    align-items: center;
    justify-content: center;
    gap: 40px;
  }
  .card {
    position: relative;
    width: 700px;
    height: 400px;
    background: linear-gradient(135deg, var(--card-green) 0%, var(--card-green-light) 100%);
    border-bottom: 5px solid var(--accent-yellow);
  }
  .brand {
    display: flex;
    align-items: center;
    gap: 18px;
  }
  .brand-dot {
    width: 70px;
    height: 70px;
    border-radius: 50%;
    background: var(--accent-yellow);
    flex: none;
  }
  .brand-name {
    color: var(--accent-yellow);
    font-weight: 700;
    font-size: 46px;
    letter-spacing: 1px;
    white-space: nowrap;
  }
  .card-front {
    display: flex;
    align-items: center;
    justify-content: center;
  }
  .card-back {
    display: flex;
    align-items: center;
    padding: 0 50px;
  }
  .card-back .brand-dot { width: 58px; height: 58px; }
  .card-back .brand-name { font-size: 36px; }
  .divider {
    width: 2px;
    height: 150px;
    background: var(--accent-yellow);
    margin: 0 36px;
    flex: none;
  }
  .contact-name {
    color: var(--accent-yellow);
    font-weight: 700;
    font-size: 26px;
    letter-spacing: 0.5px;
    white-space: nowrap;
  }
  .contact-role {
    color: var(--text-white);
    font-weight: 500;
    font-size: 17px;
    margin-bottom: 26px;
  }
  .contact-list { list-style: none; }
  .contact-list li {
    display: flex;
    align-items: center;
    gap: 10px;
    color: var(--text-white);
    font-weight: 500;
    font-size: 17px;
    line-height: 1.8;
    white-space: nowrap;
  }
  .contact-list svg { width: 13px; height: 13px; flex: none; }
</style>
</head>
<body>
<main class="stage">
  <section class="card card-front">
    <div class="brand">
      <span class="brand-dot"></span>
      <span class="brand-name">NUR-TIWAS</span>
    </div>
  </section>

  <section class="card card-back">
    <div class="brand">
      <span class="brand-dot"></span>
      <span class="brand-name">NUR-TIWAS</span>
    </div>
    <div class="divider"></div>
    <div class="contact">
      <p class="contact-name">IBRAHIM SUKRI</p>
      <p class="contact-role">Director</p>
      <ul class="contact-list">
        <li>
          <svg viewBox="0 0 16 16" fill="var(--accent-yellow)"><path d="M3.5 1l2.5 3-1.5 1.6c.8 2 2.4 3.6 4.4 4.4L10.5 8.5l3 2.5-1.5 3c-6 .4-11-4.6-11-11z"/></svg>
          87260413
        </li>
        <li>
          <svg viewBox="0 0 16 16" fill="none" stroke="var(--accent-yellow)" stroke-width="1.6"><rect x="1.5" y="3.5" width="13" height="9"/><path d="M1.5 3.5l6.5 5 6.5-5"/></svg>
          tkr27@velmorix.com.sg
        </li>
      </ul>
    </div>
  </section>
</main>
</body>
</html>
```